Web site homepage

I need a new homepage designing for a consumer based IT project

The obvious web sites I like are comparison sites, as they clearly work. See http://www.pricelarder.example/shopping/ca/anti-virus-security-data-protection-c610167/

However this isn’t as clean as it could be as its not their primary revenue stream. However the “results” page for one of the internal pages, should have a theme like this. You will see that by clicking on the product’s image, it takes you straight to the vendor’s check out page – which is exactly the same for the results by on my web site.

Although a completely different market, I like the https://www.quellbrook.example/ web site for its simplicity in selecting your product (pay day loan amount), through to transaction completion. Has a very consumer and friendly feel to it.

I have attached some previous designs which were ok, but not great. I don't want the 4 boxes in the middle anymore but I do like the feel with the top page images

I have also attached a jpeg of the logo I wish to use
Updates

Project Deadline Extended
Reason: A lot of the designs seem to have missed that I DO NOT require the 4 selection boxes as provided in the previous designs I issued as a guide. I am subsequently getting a lot of designs that contain this. I also seem to have a lot of designs which include product images. I DO NOT want these (at this time). The initial purpose of the site is informational. I am extending the deadline so that I can give feedback to each design and for you to provide a response. I will not extend past these extra 5 days. Thanks

Hello designers, Thank you all for the efforts you have gone to, it is appreciated. I have reviewed each an every design giving my honest feedback. If you have not received the feedback, please contact me. I have extended the deadline - and WILL NOT be extending this any further. I will be reviewing each updated design at this time every evening until the contest closes to give you the feedback as quickly as possible. Thanks for your efforts and please contact me to discuss any points. Gareth.

Target Market(s)

Shieldwise Hub will be an affiliate based web site providing a product comparison-based service for the consumer market, specifically for the UK. Target audience is 100% consumer and should be easy, friendly and memorable for the user.

Industry/Entity Type

Loan

Font styles to use
Sans Serif

Colors

Designer to choose colors to be used in the design.

Requirements
Must have
• Much be a bold, friendly and simple layout
Should not have
• corporate feel. must be consumer focused. bold and simple

```html
<!DOCTYPE html>
<html lang="en">
<head>
<meta charset="utf-8">
<title>Shieldwise Hub – Compare Computer Security Software</title>
<link href="https://fonts.googleapis.com/css2?family=Open+Sans:ital,wght@0,300;0,400;1,300&family=Roboto:wght@400;500&display=swap" rel="stylesheet">
<style>
  :root {
    --navy: #1f4f8f;
    --navy-deep: #235592;
    --amber: #fdb515;
    --ink: #333333;
    --muted: #555555;
    --rule: #d9d9d9;
    --paper: #ffffff;
  }
  * { box-sizing: border-box; margin: 0; padding: 0; }
  html, body { width: 1200px; height: 713px; overflow: hidden; background: var(--paper); }
  .page { position: relative; width: 1200px; height: 713px; font-family: "Open Sans", sans-serif; }

  .hero-title {
    position: absolute; top: 58px; left: 0; width: 100%; text-align: center;
    font-weight: 300; font-size: 35px; color: var(--navy); letter-spacing: 0.2px;
  }
  .hero-tagline {
    position: absolute; top: 98px; left: 0; width: 100%; text-align: center;
    font-weight: 300; font-style: italic; font-size: 27px; color: var(--amber);
  }

  .feature { position: absolute; top: 197px; width: 300px; text-align: center; }
  .feature-icon {
    width: 92px; height: 92px; border-radius: 50%; margin: 0 auto;
    display: flex; align-items: center; justify-content: center;
  }
  .feature-icon.amber { background: var(--amber); }
  .feature-icon.navy { background: var(--navy-deep); }
  .feature-title {
    margin-top: 19px; font-family: "Roboto", sans-serif; font-weight: 500;
    font-size: 23px; color: var(--ink);
  }
  .feature-text {
    margin-top: 17px; font-family: "Roboto", sans-serif; font-size: 14.5px;
    line-height: 19px; color: var(--muted);
  }

  .connectors { position: absolute; top: 0; left: 0; }

  .cta {
    position: absolute; left: 418px; top: 582px; width: 364px; height: 73px;
    border: 1px solid var(--amber); border-radius: 6px; overflow: hidden;
    display: flex; align-items: stretch; text-decoration: none; background: var(--paper);
  }
  .cta-brand {
    width: 79px; background: var(--amber); color: var(--paper);
    display: flex; align-items: center; justify-content: center; text-align: center;
    font-family: "Open Sans", sans-serif; font-weight: 400; font-size: 12px; line-height: 15px;
  }
  .cta-label {
    flex: 1; display: flex; align-items: center; padding-left: 28px;
    font-weight: 300; font-size: 29px; color: var(--navy);
  }

  .footer-rule { position: absolute; left: 0; top: 710px; width: 100%; height: 1px; background: var(--rule); }
</style>
</head>
<body>
<main class="page">
  <h1 class="hero-title">Compare the Right Computer Security Software</h1>
  <p class="hero-tagline">... all in under 30 seconds!</p>

  <section class="feature" style="left:23px">
    <div class="feature-icon amber">
      <svg width="40" height="40" viewBox="0 0 40 40" aria-hidden="true">
        <circle cx="20" cy="13" r="8" fill="#fff"/>
        <path d="M4 35 C4 26 11 23 20 23 C29 23 36 26 36 35 Z" fill="#fff"/>
      </svg>
    </div>
    <h2 class="feature-title">We're Honest</h2>
    <p class="feature-text">Compare Antivirus Software<br>Product in 30 seconds flats!</p>
  </section>

  <section class="feature" style="left:326px">
    <div class="feature-icon navy">
      <svg width="40" height="40" viewBox="0 0 40 40" aria-hidden="true">
        <path d="M5 6 L18 20 L5 34 M19 6 L32 20 L19 34" fill="none" stroke="#fff" stroke-width="4.5" stroke-linejoin="round"/>
      </svg>
    </div>
    <h2 class="feature-title">We're Quick!</h2>
    <p class="feature-text">Compare Antivirus Software<br>Product in 30 seconds flats!</p>
  </section>

  <section class="feature" style="left:592px">
    <div class="feature-icon navy">
      <svg width="40" height="40" viewBox="0 0 40 40" aria-hidden="true">
        <rect x="5" y="4" width="30" height="30" rx="2" fill="none" stroke="#fff" stroke-width="2.5"/>
        <circle cx="21" cy="19" r="7" fill="none" stroke="#fff" stroke-width="2.5"/>
        <circle cx="21" cy="19" r="2.5" fill="#fff"/>
        <path d="M9 10 V14 M9 24 V28 M9 36 V34 M31 36 V34" stroke="#fff" stroke-width="2.5"/>
      </svg>
    </div>
    <h2 class="feature-title">We're Safe!</h2>
    <p class="feature-text">You buy directly from the<br>Antivirus Provider</p>
  </section>

  <section class="feature" style="left:863px">
    <div class="feature-icon amber">
      <svg width="40" height="40" viewBox="0 0 40 40" aria-hidden="true">
        <circle cx="20" cy="20" r="16" fill="none" stroke="#fff" stroke-width="3"/>
        <text x="20" y="27" text-anchor="middle" font-family="Roboto, sans-serif" font-weight="500" font-size="20" fill="#fff">$</text>
      </svg>
    </div>
    <h2 class="feature-title">We're Cheap!</h2>
    <p class="feature-text">You get the best price,from the<br>people that made the product.</p>
  </section>

  <svg class="connectors" width="1200" height="713" viewBox="0 0 1200 713" aria-hidden="true">
    <g fill="none" stroke-width="3.5" stroke-linecap="round">
      <path stroke="var(--amber)" d="M182 406 V492 Q182 509 200 509 H590 Q604 509 607 519"/>
      <path stroke="var(--amber)" d="M1031 406 V492 Q1031 509 1013 509 H624 Q610 509 607 519"/>
      <path stroke="var(--navy-deep)" d="M481 408 V482 Q481 498 497 498 H592 Q604 498 607 508"/>
      <path stroke="var(--navy-deep)" d="M735 408 V482 Q735 498 719 498 H622 Q610 498 607 508"/>
      <path stroke="var(--navy-deep)" d="M607 510 V580"/>
    </g>
  </svg>

  <a class="cta" href="#start">
    <span class="cta-brand">Shieldwise<br>Hub</span>
    <span class="cta-label">Get Started Now!</span>
  </a>

  <div class="footer-rule"></div>
</main>
</body>
</html>
```